Business Card Design Project

Business card design with a funky, clean, modern design. Business is an immigration consultancy. Client base will be Canadian employers wanting to hire or retain foreign workers and foreign nationals wanting to immigrate to Canada.

Full color possible, but should incorporate red/white/black as per the logo to be provided. Double sided card design.

Target Market(s)

Canadian employers looking to hire/retain staff and also foreign nationals immigrating to Canada

Industry/Entity Type

Business

Requirements
Must have
• Logo (to be provided)
Name (Marla Quintero, Immigration Consultant)
Phone (604) 517-3362
E-mail: marla@lanternpathvisas.example
Web: www.lanternpathvisas.example

Nice to have
• Tag Line
Clean, modern style

```html
<!DOCTYPE html>
<html lang="en">
<head>
<meta charset="utf-8">
<title>Lantern Path Visas – Business Card</title>
<link rel="stylesheet" href="https://fonts.googleapis.com/css2?family=Tinos:wght@400;700&display=swap">
<style>
  :root {
    --backdrop: #d9d9db;
    --card: #fbfbf9;
    --ink: #1d1d1d;
    --red: #d3191f;
    --red-soft: #e8652f;
    --shadow: rgba(0, 0, 0, 0.18);
  }
  * { margin: 0; padding: 0; box-sizing: border-box; }
  html, body {
    width: 1200px;
    height: 1200px;
    overflow: hidden;
    background: var(--backdrop);
    font-family: "Tinos", "Times New Roman", serif;
    color: var(--ink);
  }
  .canvas { position: relative; width: 1200px; height: 1200px; }

  .card {
    position: absolute;
    left: 160px;
    width: 880px;
    height: 503px;
    background: var(--card);
    box-shadow: 0 10px 30px var(--shadow);
  }
  .card--back { top: 70px; }
  .card--front { top: 627px; }

  /* brand name block */
  .brand {
    position: absolute;
    display: flex;
    align-items: center;
    gap: 22px;
  }
  .brand__dot {
    border-radius: 50%;
    background: var(--red);
    flex: none;
  }
  .brand__name {
    font-weight: 700;
    color: var(--ink);
    line-height: 0.95;
    letter-spacing: 1px;
    text-transform: uppercase;
  }

  .card--back .brand { left: 60px; top: 50px; }
  .card--back .brand__name { font-size: 52px; }
  .card--back .brand__mark {
    position: absolute;
    right: 90px;
    bottom: 70px;
    width: 300px;
    height: 300px;
    border-radius: 50%;
    background: var(--red);
  }

  .card--front .brand { left: 55px; top: 50px; }
  .card--front .brand__dot { width: 74px; height: 74px; }
  .card--front .brand__name { font-size: 36px; }

  .holder {
    position: absolute;
    right: 60px;
    top: 150px;
    text-align: right;
  }
  .holder__name { font-size: 38px; font-weight: 400; }
  .holder__title { font-size: 26px; color: var(--red); margin-top: 4px; }

  .rule {
    position: absolute;
    left: 55px;
    right: 120px;
    top: 290px;
    height: 3px;
    background: linear-gradient(90deg, rgba(211,25,31,0) 0%, var(--red) 45%, var(--red-soft) 70%, rgba(232,101,47,0) 100%);
  }

  .contact {
    position: absolute;
    display: flex;
    align-items: center;
    gap: 12px;
    font-size: 22px;
    white-space: nowrap;
  }
  .contact svg { width: 22px; height: 22px; fill: none; stroke: var(--ink); stroke-width: 2; flex: none; }
  .contact--phone { left: 330px; top: 245px; }
  .contact--email { left: 55px; top: 312px; }
  .contact--web { right: 60px; top: 390px; }
</style>
</head>
<body>
<main class="canvas">

  <section class="card card--back" aria-label="Card back">
    <div class="brand">
      <span class="brand__name">Lantern Path<br>Visas</span>
    </div>
    <div class="brand__mark" aria-hidden="true"></div>
  </section>

  <section class="card card--front" aria-label="Card front">
    <div class="brand">
      <span class="brand__dot" aria-hidden="true"></span>
      <span class="brand__name">Lantern Path<br>Visas</span>
    </div>

    <div class="holder">
      <p class="holder__name">Marla Quintero</p>
      <p class="holder__title">RCIC</p>
    </div>

    <div class="contact contact--phone">
      <svg viewBox="0 0 24 24" aria-hidden="true"><rect x="6" y="2" width="12" height="20" rx="2"/><line x1="10" y1="18" x2="14" y2="18"/></svg>
      <span>(604) 517-3362</span>
    </div>

    <div class="rule" aria-hidden="true"></div>

    <div class="contact contact--email">
      <svg viewBox="0 0 24 24" aria-hidden="true"><rect x="2" y="5" width="20" height="14" rx="1"/><polyline points="2,6 12,13 22,6"/></svg>
      <span>marla@lanternpathvisas.example</span>
    </div>

    <div class="contact contact--web">
      <svg viewBox="0 0 24 24" aria-hidden="true"><polygon points="3,11 21,3 13,21 11,13" fill="#1d1d1d"/></svg>
      <span>www.lanternpathvisas.example</span>
    </div>
  </section>

</main>
</body>
</html>
```